Paint Protection Options

This is a flyer that will describe two different paint protection options for vehicles. I have mocked up a Word doc. As well, I've included some samples of other flyers where I like the "look". I am not locked into any single layout or design. In my Word doc I have them side-by-side. I think that makes sense but open to ideas. I've also added some pics of the two options being applied to cars. We need to have one of each (ceramic and ppf) at a minimum. In the grid I'm thinking different colors dots/circles to differentiate the different levels. But again, I'm open to suggestions. You can use the symbol for microns in the grid under the Thickness row. I spelled it out because I didn't know how to insert.

```html
<!DOCTYPE html>
<html lang="en">
<head>
<meta charset="utf-8">
<title>Paint Protection Options</title>
<link href="https://fonts.googleapis.com/css2?family=Montserrat:wght@400;500;600;700;800&display=swap" rel="stylesheet">
<style>
  :root {
    --red: #e0161e;
    --black: #121212;
    --ink: #1d1d1d;
    --muted: #4a4a4a;
    --white: #ffffff;
    --rule: #d9d9d9;
    --row-a: #2a2a2a;
    --row-b: #1a1a1a;
    --stage: #e9e9e9;
    --dot-low: #9a9a9a;
    --dot-mid: #f2a81d;
    --dot-high: #2fb34a;
  }
  * { box-sizing: border-box; margin: 0; padding: 0; }
  html, body { width: 755px; height: 1200px; overflow: hidden; background: var(--stage); }
  body { font-family: "Montserrat", Arial, sans-serif; color: var(--ink); }

  .sheet {
    position: absolute; left: 169px; width: 417px; height: 590px;
    background: var(--white); overflow: hidden;
    box-shadow: 0 2px 8px rgba(0,0,0,.15);
  }
  .sheet.front { top: 6px; }
  .sheet.back { top: 604px; }

  /* front */
  .hero-photo {
    position: absolute; left: 0; top: 0; width: 417px; height: 282px;
    background:
      radial-gradient(ellipse at 65% 85%, #c8141b 0%, #8a0c10 30%, transparent 55%),
      radial-gradient(ellipse at 35% 35%, #3a3f48 0%, #1b1e24 45%, #0b0c0f 100%);
  }
  .title-band {
    position: absolute; left: 0; top: 272px; width: 386px; height: 38px;
    background: var(--red); display: flex; align-items: center; padding-left: 20px;
  }
  .title-band h1 { color: var(--white); font-weight: 800; font-size: 18px; text-transform: uppercase; letter-spacing: .3px; }

  .options {
    position: absolute; left: 18px; top: 324px; width: 381px;
    display: grid; grid-template-columns: 1fr 1fr; column-gap: 18px;
  }
  .option h2 { font-size: 11.5px; font-weight: 700; color: var(--black); line-height: 1.25; }
  .option .bar { width: 28px; height: 2px; background: var(--red); margin: 5px 0 7px; }
  .option p { font-size: 6.8px; line-height: 1.6; color: var(--muted); margin-bottom: 6px; }
  .features { list-style: none; margin-top: 4px; }
  .features li {
    display: flex; align-items: center; gap: 5px;
    font-size: 6.8px; font-weight: 600; color: var(--ink);
    padding: 4px 0; border-bottom: 1px solid var(--rule);
  }
  .features svg { flex: none; }

  .footer {
    position: absolute; left: 0; bottom: 0; width: 417px; height: 34px;
    background: var(--black); border-top: 3px solid var(--red);
    display: flex; align-items: center; justify-content: space-between; padding: 0 18px;
  }
  .contact { display: flex; align-items: center; gap: 6px; color: var(--white); font-size: 8px; font-weight: 600; }
  .contact .icon { width: 16px; height: 16px; border-radius: 50%; background: var(--red); display: flex; align-items: center; justify-content: center; }

  /* back */
  .detail-photo {
    position: absolute; left: 0; top: 0; width: 417px; height: 188px;
    background: radial-gradient(ellipse at 50% 40%, #4a5260 0%, #1f242c 55%, #0c0e12 100%);
  }
  .compare {
    position: absolute; left: 18px; top: 200px; width: 381px;
    border-collapse: collapse; font-size: 6.5px; color: var(--white);
  }
  .compare th {
    background: var(--red); font-weight: 700; text-align: left;
    padding: 0 6px; height: 20px;
  }
  .compare td { padding: 0 6px; height: 17px; font-weight: 500; }
  .compare tbody tr:nth-child(odd) td { background: var(--row-a); }
  .compare tbody tr:nth-child(even) td { background: var(--row-b); }
  .compare td:first-child { font-weight: 600; width: 31%; }
  .dots { display: inline-flex; gap: 3px; vertical-align: middle; }
  .dot { width: 7px; height: 7px; border-radius: 50%; display: inline-block; }
  .dot.low { background: var(--dot-low); }
  .dot.mid { background: var(--dot-mid); }
  .dot.high { background: var(--dot-high); }
  .dot.off { background: #555; }

  .gallery {
    position: absolute; left: 18px; top: 388px; width: 381px; height: 150px;
    display: grid; grid-template-columns: 1fr 1fr; column-gap: 8px;
  }
  .gallery .shot { background: linear-gradient(135deg, #2a2e35 0%, #6a6f77 45%, #c0161c 100%); }
  .gallery .shot.film { background: linear-gradient(135deg, #1d2026 0%, #7a8088 50%, #d6dade 100%); }
</style>
</head>
<body>

<main class="sheet front">
  <div class="hero-photo" role="img" aria-label="Detailer in gloves and mask polishing the bonnet of a red car in a workshop"></div>
  <div class="title-band"><h1>Paint Protection Options</h1></div>

  <section class="options">
    <article class="option">
      <h2>Ceramic Coatings</h2>
      <div class="bar"></div>
      <p>A ceramic coating is a liquid polymer that bonds with your factory paint, forming a hard, glossy layer that repels water, dirt and road grime while making every wash faster and easier.</p>
      <p>Ideal for drivers who want lasting shine and simple upkeep without the added thickness of film.</p>
      <ul class="features">
        <li><svg width="9" height="9" viewBox="0 0 16 16"><circle cx="8" cy="8" r="8" fill="#e0161e"/><path d="M4.5 8.2l2.3 2.3 4.7-4.8" stroke="#fff" stroke-width="2" fill="none"/></svg>Deep gloss and rich color</li>
        <li><svg width="9" height="9" viewBox="0 0 16 16"><circle cx="8" cy="8" r="8" fill="#e0161e"/><path d="M4.5 8.2l2.3 2.3 4.7-4.8" stroke="#fff" stroke-width="2" fill="none"/></svg>Hydrophobic, easy-clean surface</li>
        <li><svg width="9" height="9" viewBox="0 0 16 16"><circle cx="8" cy="8" r="8" fill="#e0161e"/><path d="M4.5 8.2l2.3 2.3 4.7-4.8" stroke="#fff" stroke-width="2" fill="none"/></svg>Resists UV and chemical stains</li>
      </ul>
    </article>

    <article class="option">
      <h2>Paint Protection Film (PPF)</h2>
      <div class="bar"></div>
      <p>Paint protection film is a clear, self-healing urethane layer applied over painted panels to guard against stone chips, scratches and swirl marks from everyday driving.</p>
      <p>Best for high-impact areas such as bumpers, hoods and mirrors, or full-body coverage.</p>
      <ul class="features">
        <li><svg width="9" height="9" viewBox="0 0 16 16"><circle cx="8" cy="8" r="8" fill="#e0161e"/><path d="M4.5 8.2l2.3 2.3 4.7-4.8" stroke="#fff" stroke-width="2" fill="none"/></svg>Blocks chips and scratches</li>
        <li><svg width="9" height="9" viewBox="0 0 16 16"><circle cx="8" cy="8" r="8" fill="#e0161e"/><path d="M4.5 8.2l2.3 2.3 4.7-4.8" stroke="#fff" stroke-width="2" fill="none"/></svg>Heals light marks with heat</li>
        <li><svg width="9" height="9" viewBox="0 0 16 16"><circle cx="8" cy="8" r="8" fill="#e0161e"/><path d="M4.5 8.2l2.3 2.3 4.7-4.8" stroke="#fff" stroke-width="2" fill="none"/></svg>Nearly invisible finish</li>
      </ul>
    </article>
  </section>

  <footer class="footer">
    <div class="contact">
      <span class="icon"><svg width="9" height="9" viewBox="0 0 24 24"><path d="M12 2a7 7 0 0 0-7 7c0 5 7 13 7 13s7-8 7-13a7 7 0 0 0-7-7zm0 9.5A2.5 2.5 0 1 1 12 6.5a2.5 2.5 0 0 1 0 5z" fill="#fff"/></svg></span>
      www.glossguardauto.com
    </div>
    <div class="contact">
      <span class="icon"><svg width="9" height="9" viewBox="0 0 24 24"><path d="M6.6 10.8a15.1 15.1 0 0 0 6.6 6.6l2.2-2.2a1 1 0 0 1 1-.25 11.4 11.4 0 0 0 3.6.57 1 1 0 0 1 1 1V20a1 1 0 0 1-1 1A17 17 0 0 1 3 4a1 1 0 0 1 1-1h3.5a1 1 0 0 1 1 1c0 1.25.2 2.45.57 3.57a1 1 0 0 1-.25 1z" fill="#fff"/></svg></span>
      +91-9876501234
    </div>
  </footer>
</main>

<main class="sheet back">
  <div class="detail-photo" role="img" aria-label="Gloved hands applying a coating to a car panel with a small applicator"></div>

  <table class="compare">
    <thead>
      <tr><th>Features</th><th>Car Wax</th><th>Ceramic Coating</th><th>Paint Protection Film</th></tr>
    </thead>
    <tbody>
      <tr><td>Protection Level</td>
        <td><span class="dots"><span class="dot low"></span><span class="dot off"></span><span class="dot off"></span></span></td>
        <td><span class="dots"><span class="dot mid"></span><span class="dot mid"></span><span class="dot off"></span></span></td>
        <td><span class="dots"><span class="dot high"></span><span class="dot high"></span><span class="dot high"></span></span></td></tr>
      <tr><td>Gloss Enhancement</td>
        <td><span class="dots"><span class="dot low"></span><span class="dot off"></span><span class="dot off"></span></span></td>
        <td><span class="dots"><span class="dot high"></span><span class="dot high"></span><span class="dot high"></span></span></td>
        <td><span class="dots"><span class="dot mid"></span><span class="dot mid"></span><span class="dot off"></span></span></td></tr>
      <tr><td>Chip Resistance</td><td>None</td><td>Minimal</td><td>Excellent</td></tr>
      <tr><td>Self-Healing</td><td>No</td><td>No</td><td>Yes, with heat</td></tr>
      <tr><td>Hydrophobic</td><td>Short term</td><td>Strong</td><td>Good</td></tr>
      <tr><td>UV Protection</td><td>Low</td><td>High</td><td>High</td></tr>
      <tr><td>Thickness</td><td>&lt; 1 µm</td><td>2–3 µm</td><td>150–200 µm</td></tr>
      <tr><td>Lifespan</td><td>1–3 months</td><td>2–5 years</td><td>5–10 years</td></tr>
      <tr><td>Maintenance</td><td>Frequent</td><td>Low</td><td>Low</td></tr>
    </tbody>
  </table>

  <div class="gallery">
    <div class="shot" role="img" aria-label="Ceramic coating being wiped onto a red car panel"></div>
    <div class="shot film" role="img" aria-label="Clear protection film being squeegeed onto a car body"></div>
  </div>

  <footer class="footer">
    <div class="contact">
      <span class="icon"><svg width="9" height="9" viewBox="0 0 24 24"><path d="M12 2a7 7 0 0 0-7 7c0 5 7 13 7 13s7-8 7-13a7 7 0 0 0-7-7zm0 9.5A2.5 2.5 0 1 1 12 6.5a2.5 2.5 0 0 1 0 5z" fill="#fff"/></svg></span>
      www.glossguardauto.com
    </div>
    <div class="contact">
      <span class="icon"><svg width="9" height="9" viewBox="0 0 24 24"><path d="M6.6 10.8a15.1 15.1 0 0 0 6.6 6.6l2.2-2.2a1 1 0 0 1 1-.25 11.4 11.4 0 0 0 3.6.57 1 1 0 0 1 1 1V20a1 1 0 0 1-1 1A17 17 0 0 1 3 4a1 1 0 0 1 1-1h3.5a1 1 0 0 1 1 1c0 1.25.2 2.45.57 3.57a1 1 0 0 1-.25 1z" fill="#fff"/></svg></span>
      +91-9876501234
    </div>
  </footer>
</main>

</body>
</html>
```